Pemberton Dialworks Business Card Design

Double Sided Business Card Design for a Locksmith company specializing in Safecracking, safe & vault service.

```html
<!DOCTYPE html>
<html lang="en">
<head>
<meta charset="utf-8">
<title>Pemberton Dialworks Business Card</title>
<link href="https://fonts.googleapis.com/css2?family=Archivo:wght@400;800&display=swap" rel="stylesheet">
<style>
  :root {
    --green: #2a7d43;
    --ink: #222222;
    --paper: #f6f6f4;
    --backdrop: #dedede;
    --rule: #9a9a9a;
  }
  * { margin: 0; padding: 0; box-sizing: border-box; }
  html, body { width: 1200px; height: 930px; overflow: hidden; }
  body {
    background: var(--backdrop);
    font-family: "Archivo", Arial, sans-serif;
    position: relative;
  }
  .card {
    position: absolute;
    left: 270px;
    width: 660px;
    height: 377px;
    box-shadow: 0 6px 18px rgba(0,0,0,0.12);
  }
  .card--front { top: 52px; background: var(--paper); }
  .card--back { top: 500px; background: var(--green); }

  .brand {
    position: absolute;
    display: flex;
    align-items: center;
    gap: 18px;
  }
  .brand__dot { width: 92px; height: 92px; border-radius: 50%; flex: none; }
  .brand__name {
    font-weight: 800;
    font-size: 38px;
    line-height: 1.02;
    letter-spacing: 1px;
    text-transform: uppercase;
  }
  .card--front .brand { left: 150px; top: 58px; }
  .card--front .brand__dot { background: var(--green); }
  .card--front .brand__name { color: var(--green); }
  .card--back .brand { left: 150px; top: 142px; }
  .card--back .brand__dot { background: #ffffff; }
  .card--back .brand__name { color: #ffffff; }

  .person {
    position: absolute;
    right: 352px;
    top: 215px;
    text-align: right;
    color: var(--ink);
    font-size: 15px;
    line-height: 1.35;
  }
  .person__name {
    color: var(--green);
    font-weight: 800;
    font-size: 17px;
    text-transform: uppercase;
    letter-spacing: 0.5px;
  }
  .divider {
    position: absolute;
    left: 330px;
    top: 215px;
    width: 1px;
    height: 100px;
    background: var(--rule);
  }
  .contact {
    position: absolute;
    left: 352px;
    top: 218px;
    list-style: none;
    color: var(--ink);
    font-size: 15px;
    line-height: 1.6;
  }
  .contact li { display: flex; align-items: center; gap: 8px; }
  .contact svg { width: 14px; height: 14px; fill: var(--green); flex: none; }
</style>
</head>
<body>
  <section class="card card--front" aria-label="Card front">
    <div class="brand">
      <span class="brand__dot"></span>
      <span class="brand__name">Pemberton<br>Dialworks</span>
    </div>

    <div class="person">
      <p class="person__name">Marcus Webb</p>
      <p>Managing Director</p>
      <p>421, Address line goes here</p>
      <p>45452, Country Name</p>
    </div>

    <span class="divider"></span>

    <ul class="contact">
      <li>
        <svg viewBox="0 0 24 24"><path d="M6.6 10.8a15.1 15.1 0 0 0 6.6 6.6l2.2-2.2a1 1 0 0 1 1-.25 11.4 11.4 0 0 0 3.6.57 1 1 0 0 1 1 1V20a1 1 0 0 1-1 1A17 17 0 0 1 3 4a1 1 0 0 1 1-1h3.5a1 1 0 0 1 1 1c0 1.25.2 2.45.57 3.57a1 1 0 0 1-.25 1z"/></svg>
        044-123 456 789
      </li>
      <li>
        <svg viewBox="0 0 24 24"><path d="M7 1h10a2 2 0 0 1 2 2v18a2 2 0 0 1-2 2H7a2 2 0 0 1-2-2V3a2 2 0 0 1 2-2zm0 4v13h10V5z"/></svg>
        044-123 456 789
      </li>
      <li>
        <svg viewBox="0 0 24 24"><path d="M2 5h20v14H2zm2 2v.5l8 5 8-5V7z"/></svg>
        info@webname.com
      </li>
      <li>
        <svg viewBox="0 0 24 24"><path d="M12 2a10 10 0 1 0 0 20 10 10 0 0 0 0-20zm6.9 6h-3a15.6 15.6 0 0 0-1.4-3.6A8 8 0 0 1 18.9 8zM12 4a14 14 0 0 1 1.9 4h-3.8A14 14 0 0 1 12 4zM4.3 14a8 8 0 0 1 0-4h3.4a16.5 16.5 0 0 0 0 4zm.8 2h3a15.6 15.6 0 0 0 1.4 3.6A8 8 0 0 1 5.1 16zm3-8h-3a8 8 0 0 1 4.4-3.6A15.6 15.6 0 0 0 8.1 8zM12 20a14 14 0 0 1-1.9-4h3.8A14 14 0 0 1 12 20zm2.3-6H9.7a14.7 14.7 0 0 1 0-4h4.6a14.7 14.7 0 0 1 0 4zm.2 5.6a15.6 15.6 0 0 0 1.4-3.6h3a8 8 0 0 1-4.4 3.6zm1.8-5.6a16.5 16.5 0 0 0 0-4h3.4a8 8 0 0 1 0 4z"/></svg>
        www.websitename.com
      </li>
    </ul>
  </section>

  <section class="card card--back" aria-label="Card back">
    <div class="brand">
      <span class="brand__dot"></span>
      <span class="brand__name">Pemberton<br>Dialworks</span>
    </div>
  </section>
</body>
</html>
```